Innovative label design for premium vodka bottle

We are looking for a bottle design (with logo) for a new premium vodka company based in Uganda. We are the first company to produce a premium vodka in Uganda made exclusively with local ingredients. We want the label design to set us apart from the more traditional (read boring) designs of local packaging and bring raise the bar for Ugandan packaging design.

We will initially sell to local markets and hope to go global in two years. The vodka is called "IRONCREST" after the famous adult mountain gorillas which live in the mountains of western Uganda.

The bottle design has to be simple and appealing to both an Africana and an International consumer (tourists). Simple, clean and to the point. The main color should be green and can or cannot include a rendering of a gorilla. Silver must also be included in the design (could be printed on metallic paper). It also can include the mountain landscapes of western Uganda. But please we are also open to more creative ideas which stray from these typical images of Uganda. I will attach some images of the silverback, the mountains of Uganda and other labels of local alcoholic beverages. Must be printed on paper. Can be glossy, matte or metallic. Do not submit ideas for labels printing on transparent film.

The size of the label should be 75mm wide by 120mm high. Also attached is an image of the bottle to be used.

Text that MUST be on the label:

Ironcrest
Ultra-Premium Vodka
Produced in Uganda
Triple Distilled from Sugar Cane
42.5%ABV
700ML

Text that CAN be incorporated:
Purely Ugandan
Triple Distilled-Ten Times filtered
3X Distilled - 10X Filtered

Please feel free to contact me with any inquiries.
Updates

Project Deadline Extended
Reason: Since we cannot meet until Wednesday to consider the designs, may as well allow the crowd a couple more days of creativity. Cheers, Tam

Hi,

Thank you all for your updates. We are currently ging through the designs and hope to have a decision made by the end of the week.

Well done!

Cheers,

Tam

Target Market(s)

Upmarket Ugandans and International consumers

Industry/Entity Type

Adult

Requirements
Must have
• Must be printed on paper. Can be glossy, matte or metallic. Do not submit ideas for labels printing on transparent film.

```html
<!DOCTYPE html>
<html lang="en">
<head>
<meta charset="utf-8">
<title>Ironcrest Ultra Premium Vodka – Label</title>
<link rel="stylesheet" href="https://fonts.googleapis.com/css2?family=Almendra:wght@700&family=Tinos:wght@400;700&display=swap">
<style>
  :root {
    --stage: #0f6a7a;
    --label-green-deep: #143d28;
    --label-green-mid: #2f6e48;
    --silver-light: #e4e8eb;
    --silver-mid: #c3c9ce;
    --silver-edge: #f3f5f6;
    --silver-rule: #858d94;
    --emblem-fill: #e9ecee;
    --ink-green: #1d5634;
    --ink-grey: #737b83;
    --figure-green: #24603b;
  }
  * { box-sizing: border-box; }
  html, body {
    margin: 0;
    width: 1200px;
    height: 1073px;
    overflow: hidden;
  }
  body { background: var(--stage); }
  .vodka-label {
    position: absolute;
    left: 300px;
    top: 56px;
    width: 600px;
    height: 960px;
    display: block;
  }
  .brand-name {
    font-family: "Almendra", Georgia, serif;
    font-weight: 700;
    fill: var(--ink-green);
  }
  .label-serif { font-family: "Tinos", "Times New Roman", serif; }
  .spec { fill: var(--ink-green); font-size: 13px; }
  .product-line { fill: var(--ink-grey); font-size: 16px; font-weight: 700; }
  .process-line { fill: var(--ink-green); font-size: 12.5px; }
  .origin-line { fill: var(--ink-green); font-size: 12px; }
</style>
</head>
<body>
<svg class="vodka-label" viewBox="0 0 375 600" xmlns="http://www.w3.org/2000/svg" aria-label="Ironcrest vodka label">
  <defs>
    <linearGradient id="label-ground" x1="0" x2="1" y1="0" y2="0">
      <stop offset="0" stop-color="var(--label-green-deep)"/>
      <stop offset="0.5" stop-color="var(--label-green-mid)"/>
      <stop offset="1" stop-color="var(--label-green-deep)"/>
    </linearGradient>
    <linearGradient id="silver-sheen" x1="0" x2="1" y1="0" y2="1">
      <stop offset="0" stop-color="var(--silver-mid)"/>
      <stop offset="0.5" stop-color="var(--silver-light)"/>
      <stop offset="1" stop-color="var(--silver-mid)"/>
    </linearGradient>
    <path id="origin-arc" d="M143.5,140 A44,44 0 0 1 231.5,140"/>
  </defs>

  <rect class="label-ground" width="375" height="600" fill="url(#label-ground)"/>

  <!-- outer shield panel -->
  <path class="panel-outer"
        d="M30,150 L95,150 C115,70 150,40 187.5,40 C225,40 260,70 280,150 L345,150 A12,12 0 0 0 357,162 L357,438 A12,12 0 0 0 345,450 L280,450 C260,530 225,560 187.5,560 C150,560 115,530 95,450 L30,450 A12,12 0 0 0 18,438 L18,162 A12,12 0 0 0 30,150 Z"
        fill="url(#silver-sheen)" stroke="var(--silver-edge)" stroke-width="7"/>
  <path d="M30,150 L95,150 C115,70 150,40 187.5,40 C225,40 260,70 280,150 L345,150 A12,12 0 0 0 357,162 L357,438 A12,12 0 0 0 345,450 L280,450 C260,530 225,560 187.5,560 C150,560 115,530 95,450 L30,450 A12,12 0 0 0 18,438 L18,162 A12,12 0 0 0 30,150 Z"
        fill="none" stroke="var(--silver-rule)" stroke-width="1.2"/>

  <!-- inner text panel -->
  <path class="panel-inner"
        d="M44,185 L331,185 A10,10 0 0 0 341,195 L341,405 A10,10 0 0 0 331,415 L44,415 A10,10 0 0 0 34,405 L34,195 A10,10 0 0 0 44,185 Z"
        fill="none" stroke="var(--silver-edge)" stroke-width="3.5"/>
  <path d="M44,185 L331,185 A10,10 0 0 0 341,195 L341,405 A10,10 0 0 0 331,415 L44,415 A10,10 0 0 0 34,405 L34,195 A10,10 0 0 0 44,185 Z"
        fill="none" stroke="var(--silver-rule)" stroke-width="0.8"/>

  <!-- emblem -->
  <ellipse class="emblem" cx="187.5" cy="140" rx="62" ry="56" fill="var(--emblem-fill)" stroke="var(--silver-rule)" stroke-width="1"/>
  <text class="label-serif origin-line" text-anchor="middle">
    <textPath href="#origin-arc" startOffset="50%">Produced in Uganda</textPath>
  </text>
  <ellipse class="emblem-figure" role="img" aria-label="Illustration of a mountain gorilla" cx="189" cy="154" rx="21" ry="32" fill="var(--figure-green)"/>

  <!-- specs -->
  <text class="label-serif spec" x="48" y="216">42,5%</text>
  <text class="label-serif spec" x="327" y="216" text-anchor="end">700<tspan font-size="10">ML</tspan></text>

  <!-- brand & product -->
  <text class="brand-name" x="187.5" y="306" text-anchor="middle" font-size="44" letter-spacing="0.5">IRONCREST</text>
  <text class="label-serif product-line" x="187.5" y="340" text-anchor="middle">ULTRA PREMIUM VODKA</text>
  <text class="label-serif process-line" x="187.5" y="362" text-anchor="middle">Triple Distilled from Sugar Cane</text>
</svg>
</body>
</html>
```